New Web Site Design - Amber Ridge Telecom Solutions

We are looking for a completely new web site design. Amber Ridge Telecom Solutions is a full service company providing PBX and IP/Cloud Based phone systems. We also sell and install video camera surveillance systems and provide low voltage cabling services (CAT5 and CAT3). We are looking for something professional looking. We want to be able to showcase our vendor partners as well as be able to show photos of some of the work we have done. We will also want to be able to post PDF brochures as well as make changes to the website ourselves.

Target Market(s)

Commercial

Industry/Entity Type

Communication

Coding

Coded - Design and coding required

Number of Pages Required

5+ page

Font styles to use
Sans Serif

Colors
0455a3

Requirements
Must have
• Ability to upload PDF brochures
• Professional look and feel
• Ability to upload and easily insert job photos
• Thinking it should have at least 6 pages: Main page, phone systems and services page, carrier services page, video surveillance systems and service page, low voltage cabling services page, contact us page

```html
<!DOCTYPE html>
<html lang="en">
<head>
<meta charset="utf-8">
<title>Amber Ridge Telecom Solutions</title>
<link rel="stylesheet" href="https://fonts.googleapis.com/css2?family=Raleway:wght@400;500;600;700&display=swap">
<style>
:root{
  --navy:#12296a;
  --navy-deep:#0b1f52;
  --red:#e4212a;
  --ink:#2b2f3a;
  --grey:#8a8d94;
  --grey-light:#b4b6bb;
  --panel:#efeff0;
  --panel-2:#f6f6f7;
  --dark:#2e3138;
  --footer:#3b3e46;
  --footer-line:#52555d;
  --white:#ffffff;
}
*{margin:0;padding:0;box-sizing:border-box}
html,body{width:1200px;height:3109px;overflow:hidden}
body{font-family:"Raleway",Arial,sans-serif;color:var(--ink);background:var(--white);position:relative}
.abs{position:absolute}
ul{list-style:none}

/* header */
.site-header{position:absolute;left:0;top:0;width:1200px;height:80px;background:var(--white);box-shadow:0 2px 6px rgba(0,0,0,.08);z-index:3}
.brand-band{position:absolute;left:0;top:0}
.brand{position:absolute;left:155px;top:22px;color:var(--white)}
.brand-name{font-size:17px;font-weight:600;line-height:1.1}
.brand-name small{display:block;font-size:10px;font-weight:600;letter-spacing:.5px}
.main-nav{position:absolute;left:478px;top:28px;display:flex;gap:0}
.main-nav a{display:block;font-size:12px;font-weight:600;color:var(--navy);text-decoration:none;padding:6px 14px;letter-spacing:.3px}
.main-nav a.active{background:var(--red);color:var(--white);clip-path:polygon(8% 0,100% 0,92% 100%,0 100%);padding:6px 22px}
.social{display:flex;gap:7px}
.social span{width:22px;height:22px;border-radius:50%;background:#b7b9bd;display:block}
.social span.on{background:var(--red)}
.header-social{position:absolute;left:935px;top:30px}

/* hero */
.hero{position:absolute;left:0;top:80px;width:1200px;height:398px;background:linear-gradient(100deg,#6f95ad 0%,#8fb2c6 35%,#5b7f99 65%,#1f2d3f 100%)}
.hero-copy{position:absolute;left:155px;top:150px;color:var(--white)}
.hero-kicker{font-size:12px;font-weight:500}
.hero-title{font-size:21px;font-weight:500;margin-top:6px}
.hero-title b{font-weight:700}
.hero-sub{font-size:13px;margin-top:14px;line-height:1.4;opacity:.95}
.hero-prev{position:absolute;left:58px;top:180px}
.hero-next{position:absolute;left:1113px;top:178px;width:40px;height:40px;background:var(--red);display:flex;align-items:center;justify-content:center}
.hero-dots{position:absolute;left:1037px;top:170px;display:flex;flex-direction:column;gap:7px}
.hero-dots i{width:6px;height:6px;border-radius:50%;background:rgba(255,255,255,.6);display:block}
.hero-dots i.on{background:var(--white)}

/* section headings */
.sec-title{font-size:27px;font-weight:700;color:var(--navy-deep);letter-spacing:.3px}
.rule{display:flex;gap:0;height:3px}
.rule .r{width:28px;background:var(--red)}
.rule .g{width:26px;background:#d4d5d8}

/* welcome */
.welcome-frame{position:absolute;left:155px;top:544px;width:258px;height:250px;background:#ebebec}
.welcome-photo{position:absolute;left:183px;top:572px;width:248px;height:248px;background:linear-gradient(150deg,#eef0ea 0%,#cfd3cb 45%,#4a4c50 75%,#2d2e31 100%)}
.welcome-text{position:absolute;left:485px;top:565px;width:545px}
.welcome-text h1{font-size:28px;font-weight:700;color:var(--navy-deep);letter-spacing:.2px}
.welcome-text h2{font-size:19px;font-weight:500;color:var(--navy);margin-top:2px}
.welcome-text .rule{margin-top:16px}
.lead{font-size:13px;color:#4a4d55;margin-top:26px}
.body-copy{font-size:11px;line-height:1.5;color:var(--grey);margin-top:12px}
.btn-outline{display:inline-block;border:1px solid var(--red);color:var(--red);font-size:10px;font-weight:600;padding:7px 12px;letter-spacing:.3px}
.welcome-text .btn-outline{margin-top:34px}

/* services */
.bands{position:absolute;left:0;top:0;z-index:0}
.services{position:absolute;left:155px;top:950px;width:900px;z-index:1}
.services .sub{font-size:12px;color:var(--navy);margin-top:6px}
.services .rule{margin-top:10px}
.service-grid{display:flex;gap:0;margin-top:32px}
.service{width:305px}
.service-icon{width:100px;height:100px;border-radius:50%;background:var(--navy-deep);display:flex;align-items:center;justify-content:center}
.service-icon.red{background:var(--red)}
.service h3{font-size:17px;font-weight:500;color:#3a3d45;margin-top:26px;line-height:1.25;width:210px}
.service p{font-size:11px;line-height:1.45;color:var(--grey-light);margin-top:18px;width:250px}
.more{font-size:10px;color:var(--grey);margin-top:26px;letter-spacing:.3px}
.more.red{color:var(--red)}
.more b{margin-right:5px}

/* products */
.products-head{position:absolute;left:0;top:1480px;width:1200px;text-align:center;z-index:1}
.products-line{position:absolute;left:470px;top:1528px;width:345px;height:1px;background:#c9cacd}
.pager{display:flex;gap:8px}
.pager span{width:22px;height:22px;border:1px solid #a8aab0;display:flex;align-items:center;justify-content:center}
.pager span.red{border-color:var(--red)}
.products-pager{position:absolute;left:990px;top:1515px}
.tabs{position:absolute;left:0;top:1555px;width:1200px;text-align:center;font-size:15px;font-weight:600;color:#4a4d55}
.tabs .on{color:var(--red)}
.tabs .sep{margin:0 10px}
.product{position:absolute;top:1610px;width:206px;height:310px;text-align:center}
.product.featured{background:var(--white);box-shadow:0 2px 14px rgba(0,0,0,.14)}
.product-photo{width:150px;height:130px;margin:26px auto 0}
.product-photo.cam{background:linear-gradient(160deg,#e2e3e5 0%,#9a9da1 55%,#4a4c50 100%)}
.product-photo.cable{background:linear-gradient(160deg,#eef0ee 0%,#a6a9ad 55%,#6f8f5a 100%)}
.product h4{font-size:11px;font-weight:500;line-height:1.4;color:#4a4d55;margin:44px auto 0;width:170px}
.price{font-size:14px;font-weight:700;color:var(--red);margin-top:34px}
.product .btn-outline{margin-top:26px}

/* projects */
.projects{position:absolute;left:155px;top:2045px;z-index:2;color:var(--white)}
.projects .sec-title{color:var(--white)}
.projects p{font-size:12px;line-height:1.4;margin-top:4px}
.projects-pager{position:absolute;left:995px;top:2120px;z-index:2}
.projects-pager span{border-color:#c9cacd}
.project{position:absolute;top:2180px;width:205px;height:130px;z-index:2}
.project.p1,.project.p3{background:linear-gradient(120deg,#b9a48a 0%,#8a7a68 45%,#c8c2ba 100%)}
.project.p4{background:linear-gradient(130deg,#6a95c4 0%,#a9c6e0 50%,#d7d9dc 100%)}
.project.p2{background:linear-gradient(120deg,#e0574e 0%,#cf3b34 100%);display:flex;align-items:center;justify-content:center}

/* clients */
.clients-head{position:absolute;left:0;top:2520px;width:1200px;text-align:center}
.quote-mark{position:absolute;font-size:58px;font-weight:700;color:#d9dadc;line-height:1;font-family:Georgia,serif}
.clients-line{position:absolute;left:385px;top:2560px;width:445px;height:1px;background:#c9cacd}
.clients-pager{position:absolute;left:993px;top:2545px}
.testimonial{position:absolute;left:0;top:2588px;width:1200px;text-align:center;font-size:11px;line-height:1.5;color:var(--grey-light)}
.client-name{position:absolute;left:0;top:2632px;width:1200px;text-align:center;font-size:13px;color:var(--red)}
.client-city{position:absolute;left:0;top:2652px;width:1200px;text-align:center;font-size:11px;color:var(--grey)}

/* footer */
.site-footer{position:absolute;left:0;top:2728px;width:1200px;height:339px;background:var(--footer);color:#d8d9dc}
.foot-col h5{font-size:12px;font-weight:700;color:var(--white);letter-spacing:.3px}
.foot-col .rule{margin-top:8px;height:2px}
.foot-col .rule .g{background:#5d6068}
.brochure-thumb{position:absolute;left:0;top:70px;width:78px;height:78px;background:linear-gradient(150deg,#6aa35a 0%,#2d6b3c 50%,#e9ece6 100%)}
.brochure-text{position:absolute;left:103px;top:46px;font-size:12px;line-height:1.35;width:200px}
.btn-red{position:absolute;left:103px;top:104px;background:var(--red);color:var(--white);font-size:10px;font-weight:600;padding:6px 14px}
.foot-list{margin-top:18px;font-size:11px;line-height:1.55}
.foot-list li::before{content:"•";margin-right:8px;color:#bbb}
.foot-list li.on{color:var(--red)}
.foot-divider{position:absolute;left:155px;top:229px;width:890px;height:1px;background:var(--footer-line)}
.contact-row{position:absolute;left:155px;top:251px;display:flex;gap:28px;font-size:11px;line-height:1.4}
.contact-row div{display:flex;gap:8px;align-items:flex-start}
.footer-social{position:absolute;left:935px;top:262px}
.footer-social span{background:#8c8f95}
.copyright{position:absolute;left:0;top:3067px;width:1200px;height:42px;background:#eeeff0;font-size:11px;color:#6a6d74;padding:13px 0 0 155px}
</style>
</head>
<body>

<header class="site-header">
  <svg class="brand-band" width="440" height="80" viewBox="0 0 440 80" aria-hidden="true">
    <polygon points="0,0 440,0 395,80 0,80" fill="var(--navy-deep)"/>
  </svg>
  <div class="brand">
    <span class="brand-name">Amber Ridge<small>TELECOM SOLUTIONS</small></span>
  </div>
  <nav class="main-nav">
    <a class="active" href="#">HOME</a>
    <a href="#">COMPANY</a>
    <a href="#">PRODUCTS</a>
    <a href="#">SERVICES</a>
    <a href="#">CONTACT US</a>
  </nav>
  <div class="social header-social"><span class="on"></span><span></span><span></span><span></span></div>
</header>

<section class="hero" role="img" aria-label="Businessman touching a cloud network icon connected to glowing nodes">
  <div class="hero-copy">
    <div class="hero-kicker">Amber Ridge Telecom Solutions</div>
    <div class="hero-title"><b>IP Phone Systems</b> Technology Solutions</div>
    <div class="hero-sub">VoIP business communications solution<br>start with a solid platform</div>
  </div>
  <svg class="hero-prev" width="16" height="30" viewBox="0 0 16 30" aria-hidden="true"><polyline points="14,2 2,15 14,28" fill="none" stroke="#fff" stroke-width="2"/></svg>
  <div class="hero-dots"><i></i><i></i><i class="on"></i><i></i></div>
  <div class="hero-next"><svg width="12" height="20" viewBox="0 0 12 20" aria-hidden="true"><polyline points="2,2 10,10 2,18" fill="none" stroke="#fff" stroke-width="2"/></svg></div>
</section>

<svg class="bands" width="1200" height="3109" viewBox="0 0 1200 3109" aria-hidden="true">
  <defs>
    <radialGradient id="projGlow" cx="0.55" cy="0.45" r="0.6">
      <stop offset="0" stop-color="#5a5e66"/>
      <stop offset="1" stop-color="#25272c" stop-opacity="0"/>
    </radialGradient>
  </defs>
  <polygon points="0,905 1200,860 1200,1400 0,1360" fill="var(--panel)"/>
  <polygon points="0,905 620,960 1200,880 1200,1400 0,1360" fill="#e9e9ea"/>
  <polygon points="0,1360 1200,1400 1200,1440 0,1420" fill="var(--panel-2)"/>
  <polygon points="0,1960 1200,2080 1200,2275 0,2365" fill="var(--dark)"/>
  <polygon points="0,1960 1200,2080 1200,2275 0,2365" fill="url(#projGlow)"/>
  <polygon points="0,2365 1200,2275 1200,2330 0,2560" fill="#e3e4e6"/>
</svg>

<div class="welcome-frame"></div>
<div class="welcome-photo" role="img" aria-label="Black office desk phone with keypad"></div>
<div class="welcome-text">
  <h1>WELCOME TO AMBER RIDGE</h1>
  <h2>Communication solutions</h2>
  <div class="rule"><span class="r"></span><span class="g"></span></div>
  <p class="lead">Lorem Ipsum is simply dummy text of the printing and typesetting industry.</p>
  <p class="body-copy">Lorem Ipsum has been the industry's standard dummy text ever since the 1500s, when an unknown printer took a galley of type and scrambled it to make a type specimen book. It has survived not only five centuries, but also the leap into electronic typesetting, remaining essentially unchanged ...</p>
  <span class="btn-outline">READ MORE</span>
</div>

<section class="services">
  <h2 class="sec-title">OUR SERVICES</h2>
  <div class="sub">What we are doing?</div>
  <div class="rule"><span class="r"></span><span class="g"></span></div>
  <div class="service-grid">
    <article class="service">
      <div class="service-icon"><svg width="48" height="36" viewBox="0 0 48 36" aria-hidden="true"><path d="M12 32h26a9 9 0 0 0 0-18 13 13 0 0 0-25-2A10 10 0 0 0 12 32z" fill="#fff"/><rect x="19" y="16" width="11" height="12" rx="1" fill="var(--navy-deep)"/></svg></div>
      <h3>PBX &amp; IP/Cloud Based Phone Systems</h3>
      <p>Lorem Ipsum is simply dummy text of the printing and typesetting industry. Lorem Ipsum has been the industry's standard dummy text ever ...</p>
      <div class="more"><b>›</b>READ MORE</div>
    </article>
    <article class="service">
      <div class="service-icon red"><svg width="46" height="40" viewBox="0 0 46 40" aria-hidden="true"><rect x="6" y="8" width="30" height="14" rx="2" transform="rotate(18 21 15)" fill="#fff"/><rect x="6" y="26" width="4" height="12" fill="#fff"/><rect x="6" y="28" width="14" height="4" fill="#fff"/></svg></div>
      <h3>Video Surveillance Systems</h3>
      <p>Lorem Ipsum is simply dummy text of the printing and typesetting in dustry. Lorem Ipsum has been the industry's standard dummy text ever ...</p>
      <div class="more red"><b>›</b>READ MORE</div>
    </article>
    <article class="service">
      <div class="service-icon"><svg width="40" height="44" viewBox="0 0 40 44" aria-hidden="true"><path d="M24 8c6 6 4 14-4 18s-12 10-6 16" fill="none" stroke="#fff" stroke-width="4" stroke-linecap="round"/><rect x="20" y="2" width="12" height="9" rx="1" transform="rotate(40 26 6)" fill="#fff"/></svg></div>
      <h3>Low Voltage Cabling (CAT5 and CAT3),</h3>
      <p>Lorem Ipsum is simply dummy text of the printing and typesetting industry. Lorem Ipsum has been the industry's standard dummy text ever ...</p>
      <div class="more"><b>›</b>READ MORE</div>
    </article>
  </div>
</section>

<div class="products-head"><h2 class="sec-title">PRODUCTS</h2></div>
<div class="products-line"></div>
<div class="pager products-pager">
  <span class="red"><svg width="12" height="10" viewBox="0 0 12 10" aria-hidden="true"><polyline points="5,1 1,5 5,9" fill="none" stroke="var(--red)" stroke-width="1.5"/><line x1="1" y1="5" x2="11" y2="5" stroke="var(--red)" stroke-width="1.5"/></svg></span>
  <span><svg width="12" height="10" viewBox="0 0 12 10" aria-hidden="true"><polyline points="7,1 11,5 7,9" fill="none" stroke="#8a8d94" stroke-width="1.5"/><line x1="1" y1="5" x2="11" y2="5" stroke="#8a8d94" stroke-width="1.5"/></svg></span>
</div>
<div class="tabs"><span class="on">VIDEO CAMERA</span><span class="sep">/</span><span>LOW VOLTAGE CABLE</span></div>

<article class="product" style="left:147px">
  <div class="product-photo cam" role="img" aria-label="White bullet security camera on wall bracket"></div>
  <h4>Vistara VX-5301 5MP Mini-Dome WiFi Camera</h4>
  <div class="price">$299.99</div>
</article>
<article class="product featured" style="left:383px">
  <div class="product-photo cable" role="img" aria-label="Coiled black low voltage cable with green label"></div>
  <h4>Lumaline Low Voltage Garden Lighting Extension Cable 15m SPT 2</h4>
  <span class="btn-outline">GET QUOTE</span>
</article>
<article class="product" style="left:612px">
  <div class="product-photo cam" role="img" aria-label="White bullet security camera on wall bracket"></div>
  <h4>Vistara VX-5301 5MP Mini-Dome WiFi Camera</h4>
  <div class="price">$529.99</div>
</article>
<article class="product" style="left:840px">
  <div class="product-photo cable" role="img" aria-label="Coiled black low voltage cable with green label"></div>
  <h4>Lumaline Low Voltage Garden Lighting Extension Cable 15m SPT 2</h4>
  <div class="price">$109.99</div>
</article>

<section class="projects">
  <h2 class="sec-title">LATEST PROJECTS</h2>
  <p>Let's Take a Look at Some of Our Best &amp; Big Project Here,<br>we love them and hope you too</p>
</section>
<div class="pager projects-pager">
  <span><svg width="12" height="10" viewBox="0 0 12 10" aria-hidden="true"><polyline points="5,1 1,5 5,9" fill="none" stroke="#ddd" stroke-width="1.5"/><line x1="1" y1="5" x2="11" y2="5" stroke="#ddd" stroke-width="1.5"/></svg></span>
  <span><svg width="12" height="10" viewBox="0 0 12 10" aria-hidden="true"><polyline points="7,1 11,5 7,9" fill="none" stroke="#fff" stroke-width="1.5"/><line x1="1" y1="5" x2="11" y2="5" stroke="#fff" stroke-width="1.5"/></svg></span>
</div>
<div class="project p1" style="left:155px" role="img" aria-label="Technician installing a camera on a stone building wall"></div>
<div class="project p2" style="left:383px" role="img" aria-label="Security cameras mounted on a wall, highlighted">
  <svg width="20" height="20" viewBox="0 0 20 20" aria-hidden="true"><path d="M3 3l14 14M17 3L3 17" stroke="#fff" stroke-width="2"/></svg>
</div>
<div class="project p3" style="left:613px" role="img" aria-label="Technician installing a camera on a stone building wall"></div>
<div class="project p4" style="left:840px" role="img" aria-label="Security cameras in front of a glass office tower"></div>

<div class="clients-head"><h2 class="sec-title">CLIENTS</h2></div>
<span class="quote-mark" style="left:325px;top:2535px">“</span>
<div class="clients-line"></div>
<span class="quote-mark" style="left:838px;top:2535px">”</span>
<div class="pager clients-pager">
  <span><svg width="12" height="10" viewBox="0 0 12 10" aria-hidden="true"><polyline points="5,1 1,5 5,9" fill="none" stroke="#8a8d94" stroke-width="1.5"/><line x1="1" y1="5" x2="11" y2="5" stroke="#8a8d94" stroke-width="1.5"/></svg></span>
  <span><svg width="12" height="10" viewBox="0 0 12 10" aria-hidden="true"><polyline points="7,1 11,5 7,9" fill="none" stroke="#8a8d94" stroke-width="1.5"/><line x1="1" y1="5" x2="11" y2="5" stroke="#8a8d94" stroke-width="1.5"/></svg></span>
</div>
<p class="testimonial">Proin sagittis feugiat elit finibus pretium. Donec et tortor non purus vulputate tincidunt. Cras congue posuer eros eget egestas.<br>Aenean varius ex ut ex laoreet fermentum. Curabitur ornare varius mi.</p>
<div class="client-name">Daniel Harlow</div>
<div class="client-city">( Melbourne )</div>

<footer class="site-footer">
  <div class="foot-col abs" style="left:155px;top:36px;width:330px;height:160px">
    <h5>PRODUCT BROCHURE</h5>
    <div class="rule"><span class="r"></span><span class="g"></span></div>
    <div class="brochure-thumb" role="img" aria-label="Product brochure cover"></div>
    <div class="brochure-text">Click here to<br>Download Product Broucher<br>with Technical Specs</div>
    <span class="btn-red">DOWNLOAD</span>
  </div>
  <div class="foot-col abs" style="left:535px;top:36px">
    <h5>QUICK LINK</h5>
    <div class="rule"><span class="r"></span><span class="g"></span></div>
    <ul class="foot-list">
      <li>Home</li><li class="on">Company</li><li>Products</li><li>Gallery</li><li>Testimonial</li><li>Contact Us</li>
    </ul>
  </div>
  <div class="foot-col abs" style="left:765px;top:36px">
    <h5>SERVICES</h5>
    <div class="rule"><span class="r"></span><span class="g"></span></div>
    <ul class="foot-list">
      <li>PBX and IP/Cloud Based phone systems</li><li>Video Camera Surveillance Systems</li><li>Low voltage Cabling</li><li>Carrier Services</li>
    </ul>
  </div>
  <div class="foot-divider"></div>
  <div class="contact-row">
    <div><svg width="10" height="13" viewBox="0 0 10 13" aria-hidden="true"><path d="M5 0a5 5 0 0 1 5 5c0 4-5 8-5 8S0 9 0 5a5 5 0 0 1 5-5z" fill="#d8d9dc"/><circle cx="5" cy="5" r="1.8" fill="var(--footer)"/></svg><span>42 Lindenweg Allee Berlin<br>Germany</span></div>
    <div><svg width="12" height="12" viewBox="0 0 12 12" aria-hidden="true"><path d="M2 1l2.5 0 1 3-1.5 1a7 7 0 0 0 3 3l1-1.5 3 1V10a1.5 1.5 0 0 1-1.5 1.5A10 10 0 0 1 .5 2.5 1.5 1.5 0 0 1 2 1z" fill="#d8d9dc"/></svg><span>+49 30 5550 1842</span></div>
    <div><svg width="13" height="10" viewBox="0 0 13 10" aria-hidden="true"><rect x="0" y="0" width="13" height="10" fill="#d8d9dc"/><polyline points="0,0 6.5,5.5 13,0" fill="none" stroke="var(--footer)" stroke-width="1.2"/></svg><span>info@amberridge-mail.com</span></div>
  </div>
  <div class="social footer-social"><span></span><span></span><span></span><span></span></div>
</footer>
<div class="copyright">© 2015 Amber Ridge Telecom Solutions. All rights reserved.</div>

</body>
</html>
```